Wordpress Design Project

Hi,

I would like a more modern colourful design doing for my website Zyl Pando (www.zy%lpando.com - remove percentage). But I do still want to keep the same sort of colors, just maybe lighter. More interesting.

I want the inside pages to NOT all look the same with just boring text.

I want the site to look more appealing and maybe a new logo.
Updates

I would like to mention I would prefer to keep the same logo after rethinking it (possibly a slight refresh of the logo if you feel its a good idea) and the same color scheme as at present.

Saves us rebranding a lot of our apps, tools online ads etc.

Also I thought it is worth mentioning we have 2 parts to the site. The front end and the logged in area. It would be good if when making the front end you keep in mind the back end at http://p.zy%lpando.com (remove percentage). We can only edit this limitedly (can edit the entire footer, the logo and full CSS of it). Would be good if we could make sure the header and footer can be used on the back end as well maybe to make it match.

I also want layouts making not just for the homepage. Obviously every page will basically be the same but I don't want all the other pages to just be 'text' and no real layout.

You can see out main pages on the website at the moment, I want those other pages to be laid out nice and differently as well. For example the testimonials page could be more interesting with speech bubbles and pictures of each person (just use placeholders). The affiliates page could be a description and then a nice fancy list of features why to join etc. 

Nothing overly complicated but I think it makes the whole site seem a lot better.

Target Market(s)

Affiliate Marketing. International.

Requirements
Must have
• Needs to be more room for links across the navigation at the top, also sub menus (at present we have a lot of pages which are hidden deep within other pages).
Nice to have
• Lists of features for advertisers and affiliates on the homepage part.

Menu items and buttons have nice hover over effects.

I want to get across on our pages all the different unique features we have.

Maybe some kind of slider which has past offer logos in, just use example logos.

```html
<!DOCTYPE html>
<html lang="en">
<head>
<meta charset="utf-8">
<title>Zyl Pando – Earn Money &amp; Increase Sales</title>
<link rel="stylesheet" href="https://fonts.googleapis.com/css2?family=Arimo:wght@400;700&display=swap">
<style>
:root{
  --blue-deep:#0f5f9e;
  --blue:#1a75bb;
  --blue-mid:#2f8bcc;
  --blue-light:#7fb8e0;
  --blue-pale:#b9d5ea;
  --orange:#f7941d;
  --orange-light:#ffb733;
  --white:#ffffff;
  --text:#333333;
  --text-soft:#555555;
  --link:#1a5f9a;
  --dark:#1c1c1c;
  --dark-grey:#4a4a4a;
}
*{box-sizing:border-box;margin:0;padding:0}
html,body{width:1018px;height:1200px;overflow:hidden}
body{
  position:relative;
  font-family:"Arimo",Arial,sans-serif;
  color:var(--text);
  background:linear-gradient(180deg,var(--white) 0,var(--white) 155px,var(--blue-pale) 155px,#a6c9e6 480px,var(--blue-light) 500px,#5aa3d8 720px,var(--blue) 900px,var(--blue-deep) 1083px);
}
.abs{position:absolute}
.top-rule{left:0;top:0;width:1018px;height:5px;background:var(--blue-deep)}

/* header */
.brand{left:155px;top:26px}
.brand-name{font-size:60px;font-weight:700;color:var(--blue);letter-spacing:1px;line-height:1}
.brand-tag{font-size:15px;font-weight:700;color:var(--blue);margin-top:6px;letter-spacing:.3px}
.ask{left:648px;top:14px;width:164px;height:40px;background:linear-gradient(var(--orange-light),var(--orange));border-radius:4px;color:var(--white);padding:3px 10px;line-height:1.1}
.ask strong{display:block;font-size:16px}
.ask span{font-size:12px}
.contact{left:652px;top:66px;font-size:12px;color:var(--text-soft);line-height:15px}
.contact .tel{font-size:18px;font-weight:700;color:var(--text);margin-bottom:4px}

/* nav */
.main-nav{left:138px;top:123px;width:743px;height:33px;display:flex;background:linear-gradient(var(--blue-mid),var(--blue-deep));border-radius:3px 3px 0 0}
.main-nav a{display:flex;align-items:center;justify-content:center;color:var(--white);font-size:13px;text-decoration:none;border-right:1px solid rgba(255,255,255,.25)}
.main-nav a.active{background:linear-gradient(var(--orange-light),var(--orange))}
.hover-note{left:370px;top:160px;font-size:8px;color:var(--text-soft)}

/* slider */
.slider{left:141px;top:164px;width:734px;height:323px;background:var(--white);border-radius:4px;box-shadow:0 3px 8px rgba(0,0,0,.25)}
.slide{left:152px;top:173px;width:719px;height:283px;background:linear-gradient(180deg,#4b8fc6,var(--blue) 60%,#1d5f99);overflow:hidden}
.slide-map{left:80px;top:35px;width:420px;height:190px;background:radial-gradient(ellipse,rgba(255,255,255,.12),transparent 70%)}
.slide-photo{left:406px;top:10px;width:250px;height:256px;background:linear-gradient(135deg,#5aa7e0,#2a2a2a 70%);border-radius:6px;opacity:.85}
.slide h1{left:19px;top:20px;font-size:36px;font-weight:400;color:var(--white)}
.slide p{left:47px;top:100px;width:340px;font-size:17px;line-height:20px;color:var(--white)}
.btn{display:inline-block;background:linear-gradient(var(--orange-light),var(--orange));color:var(--white);font-size:12px;text-align:center;border-radius:3px}
.slide .btn{left:269px;top:167px;width:89px;height:24px;line-height:24px;position:absolute}
.slide-band{left:0;top:200px;width:719px;height:1px;background:rgba(255,255,255,.3)}
.slide-cta{left:47px;top:214px;width:340px;font-size:26px;color:var(--white);line-height:29px;text-align:right}
.arrow{width:46px;height:46px;border-radius:50%;background:linear-gradient(#fff,#dcdcdc);box-shadow:0 1px 4px rgba(0,0,0,.4);display:flex;align-items:center;justify-content:center}
.arrow-left{left:144px;top:290px}
.arrow-right{left:838px;top:290px}
.dots{left:490px;top:471px;display:flex;gap:4px}
.dots i{width:8px;height:8px;border-radius:50%;background:#c8c8c8}
.dots i:first-child{background:var(--orange)}

/* feature panels */
.panel-art{left:118px;top:498px}
.feature-card{background:var(--white);border-radius:4px;width:188px;height:140px;padding:10px 12px}
.feature-card ul{list-style:none}
.feature-card li{font-size:12px;line-height:17.5px;padding-left:14px;position:relative}
.feature-card li::before{content:"";position:absolute;left:0;top:4px;border-left:7px solid var(--orange);border-top:4px solid transparent;border-bottom:4px solid transparent}
.feature-card .btn{position:absolute;bottom:8px;width:80px;height:22px;line-height:22px;font-size:12px}
.card-adv{left:145px;top:527px}
.card-adv .btn{left:102px}
.card-aff{left:687px;top:527px}
.card-aff .btn{left:96px}
.badge-label{color:var(--white);font-size:21px;font-weight:700;text-align:center;width:160px}
.label-adv{left:339px;top:580px}
.label-aff{left:519px;top:586px}

/* content boxes */
.box{background:var(--white);border-radius:5px;box-shadow:0 2px 5px rgba(0,0,0,.2)}
.welcome{left:137px;top:736px;width:480px;height:206px;padding:30px 22px}
.welcome h2{font-size:18px;font-weight:400;color:var(--text)}
.welcome h2 span{color:var(--blue)}
.welcome p{margin-top:24px;font-size:10px;line-height:13px;color:var(--text)}
.btn-blue{background:linear-gradient(var(--blue-mid),var(--blue-deep));color:var(--white);font-size:12px;border-radius:3px;width:80px;height:23px;line-height:23px;text-align:center;right:18px;bottom:18px;position:absolute}
.members{left:630px;top:736px;width:251px;height:206px}
.box-head{position:absolute;left:15px;top:10px;width:246px;height:34px;background:linear-gradient(var(--blue-mid),var(--blue-deep));color:var(--white);font-size:14px;line-height:34px;padding-left:22px}
.box-head i{position:absolute;right:14px;top:7px;width:20px;height:20px;border-radius:50%;background:#0c3f6a}
.box-head i::after{content:"";position:absolute;left:6px;top:8px;border-top:5px solid var(--white);border-left:4px solid transparent;border-right:4px solid transparent}
.login-row{position:absolute;left:16px;font-size:11px;color:var(--text)}
.login-row input{position:absolute;left:58px;top:-6px;width:164px;height:24px;border:1px solid #bbb;background:#f7f7f7}
.forgot{position:absolute;left:16px;top:136px;font-size:10px;color:var(--link);text-decoration:underline}
.members .btn{position:absolute;left:158px;top:131px;width:80px;height:22px;line-height:22px}
.register{position:absolute;left:16px;top:165px;font-size:10px;color:var(--link);text-decoration:underline}

.partners{left:137px;top:956px;width:480px;height:111px;display:flex;align-items:center;justify-content:space-between;padding:0 8px}
.partners .nav-tri{width:0;height:0;border-top:8px solid transparent;border-bottom:8px solid transparent}
.tri-l{border-right:10px solid #999}
.tri-r{border-left:10px solid #999}
.partner{font-size:14px;font-weight:700;color:#666;display:flex;align-items:center;gap:4px}
.partner b{width:16px;height:16px;background:#888;border-radius:50%;display:inline-block}

.blog{left:630px;top:956px;width:251px;height:111px}
.blog-links{position:absolute;left:16px;top:55px;font-size:10px;line-height:14px}
.blog-links a{display:block;color:var(--link)}
.follow{position:absolute;left:144px;top:52px;font-size:9px;color:var(--text)}
.socials{position:absolute;left:132px;top:68px;display:flex;gap:6px}
.socials span{width:30px;height:30px;border-radius:4px;background:var(--blue-mid)}
.socials span:nth-child(2){background:#c9302c}
.socials span:nth-child(3){background:#2d4f8f}

/* footer */
.footer-links{left:0;top:1083px;width:1018px;height:25px;background:var(--dark);display:flex;justify-content:center;gap:22px;align-items:center}
.footer-links a{color:var(--white);font-size:11px;text-decoration:none}
.footer-base{left:0;top:1108px;width:1018px;height:92px;background:linear-gradient(var(--dark-grey),#2a2a2a)}
.footer-panel{left:212px;top:1118px;width:621px;height:82px;background:linear-gradient(#fff,#dcdcdc);border-radius:30px 30px 0 0}
.apps{left:290px;top:1133px;display:flex;gap:34px}
.app{display:flex;align-items:center;gap:5px}
.app i{width:20px;height:20px;border-radius:50%;background:var(--blue)}
.app:nth-child(2) i{background:#3c9a3c}
.app:nth-child(3) i{background:var(--orange)}
.app:nth-child(4) i{background:#8bbf3a}
.app strong{display:block;font-size:9px;color:var(--link)}
.app small{display:block;font-size:6px;color:var(--text-soft)}
.copyright{left:364px;top:1171px;width:290px;height:22px;background:#2b2b2b;border-radius:3px;color:var(--white);font-size:11px;text-align:center;line-height:22px}
</style>
</head>
<body>
<div class="abs top-rule"></div>

<header>
  <div class="abs brand">
    <div class="brand-name">ZYLPANDO</div>
    <div class="brand-tag">EARN MONEY &amp; INCREASE SALES</div>
  </div>
  <div class="abs ask"><strong>Any questions?</strong><span>Call Us :</span></div>
  <div class="abs contact">
    <div class="tel">Telp :+44 (0)1632 - 960418</div>
    <div>Fax &nbsp;&nbsp;: +44 (0)1632 - 9605771</div>
    <div>Email : info@zylpando.com</div>
  </div>
  <nav class="abs main-nav">
    <a href="#" style="width:88px">HOME</a>
    <a href="#" style="width:100px">ABOUT US</a>
    <a href="#" class="active" style="width:71px">BLOG</a>
    <a href="#" style="width:128px">TESTIMONIALS</a>
    <a href="#" style="width:100px">AFFILIATES</a>
    <a href="#" style="width:115px">ADVERTISERS</a>
    <a href="#" style="width:141px;border-right:0">CONTACT US</a>
  </nav>
  <div class="abs hover-note">mouse over effect</div>
</header>

<section class="hero">
  <div class="abs slider"></div>
  <div class="abs slide">
    <div class="abs slide-map" role="img" aria-label="Faint world map backdrop"></div>
    <div class="abs slide-photo" role="img" aria-label="Hand holding banknotes reaching out of a computer monitor"></div>
    <h1 class="abs">Monetize Your Site Traffic</h1>
    <p class="abs">Lorem ipsum dolor sit amet, consecteteur adipiscing elit. set diem nonumy nibh eusmod tincidunt ut laoret dolor magna aliquam.....</p>
    <span class="btn">Read More</span>
    <div class="abs slide-band"></div>
    <div class="abs slide-cta">International Affiliate Network<br>Join Us today!</div>
  </div>
  <div class="abs arrow arrow-left"><svg width="14" height="20"><path d="M11 2 3 10l8 8" stroke="#555" stroke-width="3" fill="none"/></svg></div>
  <div class="abs arrow arrow-right"><svg width="14" height="20"><path d="M3 2l8 8-8 8" stroke="#555" stroke-width="3" fill="none"/></svg></div>
  <div class="abs dots"><i></i><i></i><i></i><i></i></div>
</section>

<section class="features">
  <svg class="abs panel-art" width="782" height="204" viewBox="0 0 782 204">
    <defs>
      <linearGradient id="panelBlue" x1="0" y1="0" x2="0" y2="1"><stop offset="0" stop-color="#2f8bcc"/><stop offset="1" stop-color="#0f5f9e"/></linearGradient>
      <radialGradient id="discBlue" cx=".45" cy=".35" r=".7"><stop offset="0" stop-color="#4aa3e0"/><stop offset="1" stop-color="#0d5592"/></radialGradient>
    </defs>
    <path d="M2 6h175l12 16h117v170H20L4 204z" fill="url(#panelBlue)"/>
    <path d="M780 10H610l-12 16H478v166h282l18 12z" fill="url(#panelBlue)"/>
    <circle cx="301" cy="95" r="82" fill="#fff"/>
    <circle cx="301" cy="95" r="74" fill="url(#discBlue)"/>
    <circle cx="481" cy="101" r="82" fill="#fff"/>
    <circle cx="481" cy="101" r="74" fill="url(#discBlue)"/>
  </svg>
  <div class="abs feature-card card-adv">
    <ul><li>Lorem ipsum dolor sit amet.</li><li>Lorem ipsum dolor sit amet.</li><li>Lorem ipsum dolor sit amet.</li><li>Lorem ipsum dolor sit amet.</li><li>Lorem ipsum dolor sit amet.</li></ul>
    <span class="btn">Sign Up Now!</span>
  </div>
  <div class="abs badge-label label-adv">ADVERTISER</div>
  <div class="abs badge-label label-aff">AFFILIATE</div>
  <div class="abs feature-card card-aff">
    <ul><li>Lorem ipsum dolor sit amet.</li><li>Lorem ipsum dolor sit amet.</li><li>Lorem ipsum dolor sit amet.</li><li>Lorem ipsum dolor sit amet.</li><li>Lorem ipsum dolor sit amet.</li></ul>
    <span class="btn">Sign Up Now!</span>
  </div>
</section>

<section class="abs box welcome">
  <h2>Welcome to <span>Zylpando.com</span></h2>
  <p>Lorem ipsum dolor sit amet, consectetuer adipiscing elit. set diem nonumy nibh euismod tincidunt ut laoreet dolor magna aliquam erat volutpat. ut wisi enim ad minim veniam. Nemo enim ipsam voluptatem quia voluptas sit aspermatur aut odit aut fugit, set quia consequuntur.<br>Lorem ipsum dolor sit amet, consectetuer adipiscing elit. set diem nonumy nibh euismod tincidunt ut laoreet dolor magna aliquam erat volutpat. ut wisi enim ad minim veniam. Nemo enim ipsam voluptatem atem quia volutpat sit aspermatur aut odit aut fugit, set wula consequuntur.</p>
  <span class="btn-blue">Read more</span>
</section>

<aside class="abs box members">
  <div class="box-head">MEMBERS AREA<i></i></div>
  <div class="login-row" style="top:64px">Email<input type="text" aria-label="Email"></div>
  <div class="login-row" style="top:94px">Password<input type="password" aria-label="Password"></div>
  <a class="forgot" href="#">Forgot Your Password?</a>
  <span class="btn">LOGIN</span>
  <a class="register" href="#">New User ? Register here</a>
</aside>

<section class="abs box partners">
  <span class="nav-tri tri-l"></span>
  <span class="partner">Vistacast</span>
  <span class="partner"><b></b>Guardo</span>
  <span class="partner">listenly.com</span>
  <span class="partner">Dishra</span>
  <span class="partner">tally now</span>
  <span class="partner"><b></b>linguaro</span>
  <span class="nav-tri tri-r"></span>
</section>

<aside class="abs box blog">
  <div class="box-head">Recent Blog Posts<i></i></div>
  <div class="blog-links"><a href="#">New Offers</a><a href="#">New Offers</a><a href="#">New Offers</a></div>
  <div class="follow">FOLLOW US ON :</div>
  <div class="socials"><span></span><span></span><span></span></div>
</aside>

<footer>
  <nav class="abs footer-links">
    <a href="#">Affiliate</a><a href="#">About Us</a><a href="#">Terms &amp; Conditions</a><a href="#">Advertiser</a><a href="#">Blogs</a><a href="#">Privacy Policy &amp; Cookies</a><a href="#">FAQ's</a><a href="#">Contact Us</a>
  </nav>
  <div class="abs footer-base"></div>
  <div class="abs footer-panel"></div>
  <div class="abs apps">
    <div class="app"><i></i><div><strong>Mobile Stats</strong><small>Track your stats on the go</small></div></div>
    <div class="app"><i></i><div><strong>Swift Browser</strong><small>Official Zyl Pando add-on</small></div></div>
    <div class="app"><i></i><div><strong>Ember Browser</strong><small>Official Zyl Pando add-on</small></div></div>
    <div class="app"><i></i><div><strong>Droidy App</strong><small>Official Zyl Pando app</small></div></div>
  </div>
  <div class="abs copyright">Copyright © 2013, zylpando.com. All rights reserved.</div>
</footer>
</body>
</html>
```